Placeholder/ebook cover to eventually become a printed book cover

Name of Book: The Shepherd's Lantern -- Corvin of Maradel
Author: H.R. Duncombe

A placeholder/email cover to become a printed book cover once the exact number of pages is known. Placeholder now, full cover in about 3-4 weeks.

Should feature an attractive 16 year male with curly black hair who lives in eastern Turkey about 45 A.D. The area has small hills and in the distance is a temple with a shimmering dome. The boy must be attractive enough to sell the book. He's probably dressed in Roman travelling clothes so no toga.

Logo has been upgraded to eventually use on spine and backcover. It's not needed for the placeholder.

Target Market(s)

Christian teen and adults

Industry/Entity Type

Book Publisher

Requirements
Must have
• An attractive hero
Nice to have
• The apostle Paul somehow incorporated

```html
<!DOCTYPE html>
<html lang="en">
<head>
<meta charset="utf-8">
<title>The Shepherd's Lantern — Corvin of Maradel</title>
<link rel="stylesheet" href="https://fonts.googleapis.com/css2?family=Open+Sans:wght@300;400;700;800&display=swap">
<style>
  :root {
    --paper-top: #f4f5f6;
    --paper-bottom: #dfe1e3;
    --teal-light: #5fc3c0;
    --teal-mid: #2f9a98;
    --teal-deep: #1c7473;
    --ring-grey: #c9cdd0;
    --swoosh-white: #ffffff;
    --title-white: #ffffff;
    --author-grey: #7d8286;
  }
  * { margin: 0; padding: 0; box-sizing: border-box; }
  html, body {
    width: 900px;
    height: 1200px;
    overflow: hidden;
  }
  body {
    font-family: "Open Sans", Arial, sans-serif;
    background: var(--paper-bottom);
  }
  .cover {
    position: relative;
    width: 900px;
    height: 1200px;
    overflow: hidden;
    background: linear-gradient(180deg, var(--paper-top) 0%, var(--paper-bottom) 100%);
  }
  .cover-shapes {
    position: absolute;
    inset: 0;
    width: 900px;
    height: 1200px;
  }
  .title-block {
    position: absolute;
    left: 118px;
    top: 395px;
    display: inline-block;
    color: var(--title-white);
  }
  .title-article {
    display: block;
    font-weight: 300;
    font-size: 86px;
    line-height: 1;
    letter-spacing: 1px;
  }
  .title-main {
    display: block;
    font-weight: 700;
    font-size: 92px;
    line-height: 1;
    margin-top: 2px;
    letter-spacing: 0;
  }
  .title-tail {
    display: block;
    text-align: right;
    font-weight: 300;
    font-size: 64px;
    line-height: 1;
    margin-top: 4px;
    letter-spacing: 1px;
  }
  .subtitle {
    display: block;
    text-align: right;
    font-weight: 400;
    font-size: 30px;
    font-variant: small-caps;
    letter-spacing: 3px;
    line-height: 1;
    margin-top: 6px;
    padding-right: 30px;
  }
  .author-line {
    position: absolute;
    right: 30px;
    bottom: 40px;
    font-weight: 400;
    font-size: 22px;
    font-variant: small-caps;
    letter-spacing: 3px;
    color: var(--author-grey);
  }
</style>
</head>
<body>
  <main class="cover">
    <svg class="cover-shapes" viewBox="0 0 900 1200" aria-hidden="true">
      <defs>
        <radialGradient id="teal-disc" cx="0.5" cy="0.5" r="0.6">
          <stop offset="0" stop-color="var(--teal-light)"/>
          <stop offset="0.6" stop-color="var(--teal-mid)"/>
          <stop offset="1" stop-color="var(--teal-deep)"/>
        </radialGradient>
      </defs>
      <!-- outer grey ring -->
      <ellipse cx="372" cy="578" rx="545" ry="500" fill="var(--ring-grey)" opacity="0.55"/>
      <!-- white separating band -->
      <ellipse cx="372" cy="578" rx="532" ry="488" fill="var(--swoosh-white)"/>
      <!-- teal disc -->
      <ellipse cx="372" cy="578" rx="520" ry="475" fill="url(#teal-disc)"/>
      <!-- lower white swoosh -->
      <path d="M0 1085 C 250 1110, 560 1060, 900 860 L 900 905 C 580 1100, 260 1150, 0 1120 Z" fill="var(--swoosh-white)" opacity="0.9"/>
      <!-- upper light arc -->
      <path d="M0 170 C 200 60, 520 40, 900 120 L 900 95 C 520 10, 210 30, 0 140 Z" fill="var(--swoosh-white)" opacity="0.7"/>
    </svg>

    <h1 class="title-block">
      <span class="title-article">THE</span>
      <span class="title-main">SHEPHERD'S</span>
      <span class="title-tail">LANTERN</span>
      <span class="subtitle">Corvin of Maradel</span>
    </h1>

    <p class="author-line">Author: H.R. Duncombe</p>
  </main>
</body>
</html>
```